Retail Seafood business needs package/label design

In need of packaging/label design for multiple seafood products such as sword fish, halibut, cod fish, scallops, mahi, catfish, and lobster tails

```html
<!DOCTYPE html>
<html lang="en">
<head>
<meta charset="utf-8">
<title>Seafood Lobster Tails Label</title>
<link rel="stylesheet" href="https://fonts.googleapis.com/css2?family=Bebas+Neue&display=swap">
<style>
  :root {
    --ink: #000000;
    --paper: #ffffff;
    --art-light: #e4e4e4;
    --art-dark: #5a5a5a;
  }
  * { margin: 0; padding: 0; box-sizing: border-box; }
  html, body {
    width: 871px;
    height: 1200px;
    overflow: hidden;
    background: var(--ink);
  }
  .label {
    position: absolute;
    left: 113px;
    top: 140px;
    width: 645px;
    height: 889px;
    background: var(--paper);
    font-family: "Bebas Neue", "Oswald", sans-serif;
    color: var(--ink);
  }
  .fresh-ribbon {
    position: absolute;
    left: 468px;
    top: 0;
    width: 117px;
    height: 111px;
  }
  .fresh-ribbon span {
    position: absolute;
    left: 0;
    right: 0;
    top: 36px;
    text-align: center;
    color: var(--paper);
    font-size: 33px;
    letter-spacing: 0.5px;
  }
  .arched-title {
    position: absolute;
    left: 0;
    top: 0;
    width: 645px;
    height: 320px;
  }
  .arched-title text {
    font-family: "Bebas Neue", "Oswald", sans-serif;
    font-size: 74px;
    letter-spacing: 18px;
    fill: var(--ink);
  }
  .product-name {
    position: absolute;
    left: 0;
    right: 0;
    top: 262px;
    text-align: center;
    font-size: 36px;
    letter-spacing: 0.5px;
    padding-left: 0;
  }
  .product-art {
    position: absolute;
    left: 156px;
    top: 323px;
    width: 333px;
    height: 247px;
    border-radius: 40% 50% 45% 40%;
    background: radial-gradient(ellipse at 50% 50%, var(--art-dark) 0%, #9a9a9a 45%, var(--art-light) 75%, var(--paper) 100%);
  }
  .tagline {
    position: absolute;
    left: 0;
    right: 0;
    top: 736px;
    text-align: center;
    font-size: 31px;
    line-height: 33px;
    letter-spacing: 5.5px;
  }
</style>
</head>
<body>
  <main class="label">
    <div class="fresh-ribbon">
      <svg width="117" height="111" viewBox="0 0 117 111" aria-hidden="true">
        <polygon points="0,0 117,0 117,111 58.5,94 0,111" fill="var(--ink)"/>
      </svg>
      <span>FRESH</span>
    </div>

    <svg class="arched-title" viewBox="0 0 645 320" aria-label="Seafood">
      <defs>
        <path id="title-arc" d="M 60 318 A 505 505 0 0 1 590 318"/>
      </defs>
      <text text-anchor="middle">
        <textPath href="#title-arc" startOffset="50%">SEAFOOD</textPath>
      </text>
    </svg>

    <h2 class="product-name">LOBSTER TAILS</h2>

    <div class="product-art" role="img" aria-label="Black and white illustration of a lobster"></div>

    <p class="tagline">AUTHENTIC SEAFOOD<br>STRAIGHT FROM<br>THE OCEAN</p>
  </main>
</body>
</html>
```